Stationery Design Project

We are looking for a full revision of our existing stationary to include within this project:

- Letterhead
- Business card
- Compliment slip

The items should be a reflection of our new website which can be found at http://www.larkfieldchecks.co.uk/

Our logo files are included within the file brief

There are some further projects which we may approach the winning designer for as we need a revision to the front cover of our reports, a new price list and two brochures for specific target markets.

Industry/Entity Type

Business

```html
<!DOCTYPE html>
<html lang="en">
<head>
<meta charset="utf-8">
<title>Larkfield Checks – Stationery Set</title>
<link href="https://fonts.googleapis.com/css2?family=PT+Sans:ital,wght@0,400;0,700;1,400&family=Arimo&display=swap" rel="stylesheet">
<style>
  :root {
    --navy: #2f3a7c;
    --sky: #0a9ad9;
    --ink: #34418a;
    --slip-title: #3f5c98;
    --paper: #ffffff;
    --backdrop-light: #8c8c8c;
    --backdrop-dark: #474747;
  }
  * { margin: 0; padding: 0; box-sizing: border-box; }
  html, body { width: 1200px; height: 885px; overflow: hidden; }
  body {
    position: relative;
    background: radial-gradient(ellipse at 50% 50%, var(--backdrop-light) 0%, var(--backdrop-dark) 100%);
    font-family: "PT Sans", sans-serif;
    color: var(--ink);
  }
  .sheet {
    position: absolute;
    background: var(--paper);
    overflow: hidden;
    box-shadow: 6px 8px 14px rgba(0,0,0,0.45);
  }
  .sheet .wave { position: absolute; left: 0; top: 0; width: 100%; height: 100%; }

  .card-front { left: 67px; top: 80px; width: 209px; height: 120px; }
  .card-back  { left: 297px; top: 80px; width: 210px; height: 120px; }
  .envelope   { left: 19px; top: 244px; width: 568px; height: 247px; }
  .slip       { left: 22px; top: 544px; width: 568px; height: 246px; }
  .letterhead { left: 628px; top: 125px; width: 504px; height: 655px; }

  .wordmark {
    position: absolute;
    font-family: "PT Sans", sans-serif;
    font-weight: 700;
    color: var(--navy);
    letter-spacing: 0.5px;
    white-space: nowrap;
    line-height: 1;
  }
  .envelope .wordmark, .slip .wordmark { left: 23px; top: 42px; font-size: 22px; }
  .letterhead .wordmark { left: 12px; top: 36px; font-size: 19px; }
  .card-front .wordmark { left: 31px; top: 58px; font-size: 12px; }
  .card-back .wordmark { left: 136px; top: 10px; font-size: 7px; color: var(--paper); }

  .contact {
    position: absolute;
    border-left: 1px solid var(--ink);
    padding-left: 7px;
    font-size: 8.5px;
    line-height: 11.5px;
    color: var(--ink);
  }
  .contact li { list-style: none; display: flex; align-items: flex-start; white-space: nowrap; }
  .contact .icon { width: 8px; height: 8px; margin-top: 2px; margin-right: 8px; flex: none; fill: var(--navy); }
  .contact .indent { padding-left: 16px; }
  .envelope .contact { left: 419px; top: 17px; padding-top: 2px; padding-bottom: 6px; }
  .slip .contact { left: 419px; top: 14px; padding-top: 2px; padding-bottom: 6px; }
  .letterhead .contact { left: 360px; top: 13px; padding-top: 2px; padding-bottom: 4px; }

  .card-back .contact {
    left: 110px; top: 31px;
    border-color: var(--paper);
    color: var(--paper);
    font-size: 5px; line-height: 6.6px;
    padding-left: 4px;
  }
  .card-back .contact .icon { width: 5px; height: 5px; margin-top: 1px; margin-right: 4px; fill: var(--paper); }
  .card-back .contact .indent { padding-left: 9px; }

  .holder { position: absolute; left: 18px; top: 29px; color: var(--paper); }
  .holder .name { font-size: 11px; line-height: 12px; }
  .holder .role { font-size: 7px; font-style: italic; text-align: right; line-height: 8px; }

  .slip-title {
    position: absolute;
    right: 18px; top: 138px;
    font-family: "Arimo", sans-serif;
    font-size: 20px;
    color: var(--slip-title);
  }
</style>
</head>
<body>

<svg width="0" height="0" style="position:absolute" aria-hidden="true">
  <defs>
    <linearGradient id="brand-blue" x1="0" y1="0" x2="1" y2="0">
      <stop offset="0" stop-color="#2f3a7c"/>
      <stop offset="0.55" stop-color="#1f6bb0"/>
      <stop offset="1" stop-color="#0a9ad9"/>
    </linearGradient>
    <symbol id="i-home" viewBox="0 0 10 10"><path d="M5 0.5 L10 5 L8.5 5 L8.5 9.5 L6 9.5 L6 6.5 L4 6.5 L4 9.5 L1.5 9.5 L1.5 5 L0 5 Z"/></symbol>
    <symbol id="i-phone" viewBox="0 0 10 10"><path d="M2 0.5 L3.8 3 L2.8 4.2 C3.6 5.8 4.4 6.6 5.8 7.2 L7 6.2 L9.5 8 L8.5 9.5 C4.5 9.5 0.5 5.5 0.5 1.5 Z"/></symbol>
    <symbol id="i-mobile" viewBox="0 0 10 10"><path d="M3 0.5 H7 V9.5 H3 Z M3.7 1.5 V7.8 H6.3 V1.5 Z"/></symbol>
    <symbol id="i-fax" viewBox="0 0 10 10"><path d="M3 0.5 H6 V3.5 H3 Z M0.5 4.5 H9.5 V9.5 H0.5 Z"/></symbol>
    <symbol id="i-mail" viewBox="0 0 10 10"><path d="M0.5 2 H9.5 V8.5 H0.5 Z M1.5 3 L5 5.8 L8.5 3 V7.5 H1.5 Z" fill-rule="evenodd"/></symbol>
    <symbol id="i-web" viewBox="0 0 10 10"><circle cx="5" cy="5" r="4.5"/><path d="M2.5 3 L4.5 3.5 L4 5.5 L5.5 7 L5 9 M6 1 L6.5 3 L8.5 4" stroke="#fff" stroke-width="0.8" fill="none"/></symbol>
  </defs>
</svg>

<!-- Business card, front -->
<section class="sheet card-front">
  <svg class="wave" viewBox="0 0 209 120" preserveAspectRatio="none" aria-hidden="true">
    <path d="M0 84 C50 80 110 108 209 97 L209 120 L0 120 Z" fill="url(#brand-blue)"/>
  </svg>
  <div class="wordmark">LARKFIELD CHECKS</div>
</section>

<!-- Business card, back -->
<section class="sheet card-back">
  <svg class="wave" viewBox="0 0 210 120" preserveAspectRatio="none" aria-hidden="true">
    <rect width="210" height="120" fill="url(#brand-blue)"/>
    <path d="M0 96 C70 104 150 96 210 88 L210 120 L0 120 Z" fill="#fff"/>
  </svg>
  <div class="wordmark">LARKFIELD CHECKS</div>
  <div class="holder">
    <div class="name">Daniel Harte</div>
    <div class="role">Director</div>
  </div>
  <ul class="contact">
    <li><svg class="icon"><use href="#i-home"/></svg>48 Fenner Street, Wattle Grove</li>
    <li class="indent">SA 5071</li>
    <li><svg class="icon"><use href="#i-mobile"/></svg>1300 555 214</li>
    <li><svg class="icon"><use href="#i-phone"/></svg>1300 555 214</li>
    <li><svg class="icon"><use href="#i-fax"/></svg>1300 555 386</li>
    <li><svg class="icon"><use href="#i-mail"/></svg>info@larkfieldchecks.com</li>
    <li><svg class="icon"><use href="#i-web"/></svg>www.larkfieldchecks.com</li>
  </ul>
</section>

<!-- Envelope -->
<section class="sheet envelope">
  <svg class="wave" viewBox="0 0 568 247" preserveAspectRatio="none" aria-hidden="true">
    <path d="M0 178 C140 150 300 232 568 188 L568 247 L0 247 Z" fill="url(#brand-blue)"/>
  </svg>
  <div class="wordmark">LARKFIELD CHECKS</div>
  <ul class="contact">
    <li><svg class="icon"><use href="#i-home"/></svg>48 Fenner Street, Wattle Grove</li>
    <li class="indent">SA 5071</li>
    <li><svg class="icon"><use href="#i-phone"/></svg>1300 555 214</li>
    <li><svg class="icon"><use href="#i-fax"/></svg>1300 555 386</li>
    <li><svg class="icon"><use href="#i-mail"/></svg>info@larkfieldchecks.com</li>
    <li><svg class="icon"><use href="#i-web"/></svg>www.larkfieldchecks.com</li>
  </ul>
</section>

<!-- Compliment slip -->
<section class="sheet slip">
  <svg class="wave" viewBox="0 0 568 246" preserveAspectRatio="none" aria-hidden="true">
    <path d="M0 177 C140 149 300 230 568 188 L568 246 L0 246 Z" fill="url(#brand-blue)"/>
  </svg>
  <div class="wordmark">LARKFIELD CHECKS</div>
  <ul class="contact">
    <li><svg class="icon"><use href="#i-home"/></svg>48 Fenner Street, Wattle Grove</li>
    <li class="indent">SA 5071</li>
    <li><svg class="icon"><use href="#i-phone"/></svg>1300 555 214</li>
    <li><svg class="icon"><use href="#i-fax"/></svg>1300 555 386</li>
    <li><svg class="icon"><use href="#i-mail"/></svg>info@larkfieldchecks.com</li>
    <li><svg class="icon"><use href="#i-web"/></svg>www.larkfieldchecks.com</li>
  </ul>
  <div class="slip-title">With Compliments</div>
</section>

<!-- Letterhead -->
<section class="sheet letterhead">
  <svg class="wave" viewBox="0 0 504 655" preserveAspectRatio="none" aria-hidden="true">
    <path d="M0 585 C120 560 280 630 504 603 L504 655 L0 655 Z" fill="url(#brand-blue)"/>
  </svg>
  <div class="wordmark">LARKFIELD CHECKS</div>
  <ul class="contact">
    <li><svg class="icon"><use href="#i-home"/></svg>48 Fenner Street, Wattle Grove</li>
    <li class="indent">SA 5071</li>
    <li><svg class="icon"><use href="#i-phone"/></svg>1300 555 214</li>
    <li><svg class="icon"><use href="#i-fax"/></svg>1300 555 386</li>
    <li><svg class="icon"><use href="#i-mail"/></svg>info@larkfieldchecks.com</li>
    <li><svg class="icon"><use href="#i-web"/></svg>www.larkfieldchecks.com</li>
  </ul>
</section>

</body>
</html>
```